Technology Solutions Provider

Let’s design a business card that will be as simple and bold at the same time. Name, email address, website & phone number.

Target Market(s)

Small to Medium Size Business

Industry/Entity Type

It Professional

Contact Information for Business Card

Name, email, website, phone numbers

Font styles to use
Sans Serif

Colors
ec1f27
f04a50
dddddd
919191
000000
ffffff

Requirements
Must have
• Clean simple look using my existing logo. I just need to the basic contact information on this card.
Nice to have
• Im considering the square size card versus the standard size business card.
Should not have
• No Mailing Address, no list of services.

```html
<!DOCTYPE html>
<html lang="en">
<head>
<meta charset="utf-8">
<title>Nova Netlink — Business Card</title>
<link rel="stylesheet" href="https://fonts.googleapis.com/css2?family=Open+Sans:wght@400;600&display=swap">
<style>
  :root {
    --red: #ec1f27;
    --red-soft: #f04a50;
    --light-grey: #dddddd;
    --mid-grey: #919191;
    --black: #000000;
    --white: #ffffff;
    --ink: #222222;
    --band-dark: #1a1718;
    --backdrop: #2a2a2a;
  }
  * { margin: 0; padding: 0; box-sizing: border-box; }
  html, body { width: 1200px; height: 1200px; overflow: hidden; }
  body {
    background: var(--backdrop);
    font-family: "Open Sans", Arial, sans-serif;
    position: relative;
  }
  .card {
    position: absolute;
    left: 180px;
    width: 840px;
    height: 480px;
    background: var(--white);
    overflow: hidden;
    box-shadow: 0 10px 30px rgba(0,0,0,0.45);
  }
  .card-front { top: 80px; }
  .card-back { top: 640px; }

  .brand { display: flex; align-items: center; gap: 12px; }
  .brand-mark {
    width: 18px; height: 18px; border-radius: 50%;
    background: var(--red);
    flex: none;
  }
  .brand-name {
    font-weight: 600;
    color: var(--red);
    letter-spacing: 1px;
    line-height: 1;
    white-space: nowrap;
  }
  .brand-tagline {
    color: var(--mid-grey);
    font-weight: 400;
    letter-spacing: 1px;
    white-space: nowrap;
  }

  /* Front */
  .card-front .brand { position: absolute; left: 60px; top: 48px; }
  .card-front .brand-name { font-size: 40px; }
  .card-front .brand-tagline {
    position: absolute; left: 90px; top: 100px; font-size: 15px;
  }
  .person { position: absolute; left: 60px; top: 140px; }
  .person-name {
    color: var(--red); font-size: 34px; font-weight: 400;
    letter-spacing: 0.5px; line-height: 1.1;
  }
  .person-role { color: var(--ink); font-size: 18px; margin-top: 2px; }
  .contact-list {
    position: absolute; left: 60px; top: 240px; list-style: none;
    font-size: 18px; color: var(--ink);
  }
  .contact-list li { display: flex; align-items: center; gap: 10px; height: 28px; white-space: nowrap; }
  .contact-list svg { width: 15px; height: 15px; fill: var(--red); flex: none; }
  .contact-rule {
    position: absolute; left: 60px; top: 336px; width: 330px;
    border-top: 1px solid var(--mid-grey);
  }
  .band-accent {
    position: absolute; left: 0; bottom: 0;
    width: 390px; height: 74px; background: var(--red);
  }
  .band-dark {
    position: absolute; left: 398px; right: 0; bottom: 0;
    height: 52px; background: var(--band-dark);
  }

  /* Back */
  .card-back .brand {
    position: absolute; left: 0; right: 0; top: 190px; justify-content: center;
  }
  .card-back .brand-name { font-size: 58px; }
  .card-back .brand-tagline {
    position: absolute; left: 0; right: 0; top: 268px;
    text-align: center; font-size: 20px;
  }
</style>
</head>
<body>

<section class="card card-front">
  <div class="brand">
    <span class="brand-mark"></span>
    <span class="brand-name">nova netlink</span>
  </div>
  <p class="brand-tagline">technology solutions provider</p>

  <div class="person">
    <h1 class="person-name">JOHN DOE</h1>
    <p class="person-role">Director</p>
  </div>

  <ul class="contact-list">
    <li>
      <svg viewBox="0 0 24 24" aria-hidden="true"><path d="M6.6 10.8a15.1 15.1 0 0 0 6.6 6.6l2.2-2.2c.3-.3.7-.4 1-.2 1.1.4 2.3.6 3.6.6.6 0 1 .4 1 1V20c0 .6-.4 1-1 1C10.6 21 3 13.4 3 4c0-.6.4-1 1-1h3.5c.6 0 1 .4 1 1 0 1.3.2 2.5.6 3.6.1.3 0 .7-.2 1z"/></svg>
      1-234-567890
    </li>
    <li>
      <svg viewBox="0 0 24 24" aria-hidden="true"><path d="M12 2a10 10 0 1 0 0 20 10 10 0 0 0 0-20zm6.9 6h-3a15.7 15.7 0 0 0-1.3-3.6A8 8 0 0 1 18.9 8zM12 4c.8 1.2 1.5 2.5 1.9 4h-3.8c.4-1.5 1.1-2.8 1.9-4zM4.3 14a8.2 8.2 0 0 1 0-4h3.4a16.5 16.5 0 0 0 0 4zm.8 2h3a15.7 15.7 0 0 0 1.3 3.6A8 8 0 0 1 5.1 16zm3-8h-3a8 8 0 0 1 4.3-3.6C8.8 5.6 8.4 6.8 8.1 8zM12 20c-.8-1.2-1.5-2.5-1.9-4h3.8c-.4 1.5-1.1 2.8-1.9 4zm2.3-6H9.7a14.7 14.7 0 0 1 0-4h4.6a14.7 14.7 0 0 1 0 4zm.3 5.6c.6-1.1 1-2.300 1.3-3.6h3a8 8 0 0 1-4.3 3.6zm1.7-5.6a16.5 16.5 0 0 0 0-4h3.4a8.2 8.2 0 0 1 0 4z"/></svg>
      www.novanetlink.com
    </li>
    <li>
      <svg viewBox="0 0 24 24" aria-hidden="true"><path d="M2 5h20v14H2zm2 2v.5l8 5 8-5V7zm0 2.8V17h16V9.8l-8 5z"/></svg>
      john@novanetlink.com
    </li>
  </ul>

  <span class="contact-rule" aria-hidden="true"></span>
  <span class="band-accent" aria-hidden="true"></span>
  <span class="band-dark" aria-hidden="true"></span>
</section>

<section class="card card-back">
  <div class="brand">
    <span class="brand-mark"></span>
    <span class="brand-name">nova netlink</span>
  </div>
  <p class="brand-tagline">technology solutions provider</p>
</section>

</body>
</html>
```